qm - website template
website of specialist in neurosurgery, and teacher at the University in Milan
qm - website template - Education
Creative Brief
Education
Benedetto L. Caramuzza, MD (specialist in neurosurgery and in the history of medicine), historian and anthropologist, teaches history of medicine and health in the Faculty of Medicine, University of Velmora Castrene, where he directs the Institute for anatomical inquiry into past doctrines "(www.dulrota.it).
He's the author of over 250 papers in national and international partner to the history of medical and health disciplines and pharmacological institute of the Italian Ombrilla.
Traditional
blu (see attached logo file)
red (see attached logo file)
We need the graphic template of: • Homepage • Generic content page (text+image+ eventual document to download) • listing page of books + page with information about the selected book • listing page of conference + page with information about the selected conference • Contact The site must be optimized for 1024X768. For the main menu, it's possibile to use not system font. File must be preferably png (adobe fireworks), otherwise ai (adobe illustrator) or psd (adobe photoshop).

```html
<!DOCTYPE html>
<html lang="en">
<head>
<meta charset="utf-8">
<title>qm – Book Listing</title>
<link href="https://fonts.googleapis.com/css2?family=Cabin:wght@400;600;700&family=Arimo:wght@400;700&display=swap" rel="stylesheet">
<style>
  :root {
    --page-bg: #efebe6;
    --panel: #ffffff;
    --nav-blue-top: #1a6aa6;
    --nav-blue-bottom: #0d4f84;
    --accent-red: #c41f2c;
    --accent-red-dark: #9e1520;
    --ink: #2a2a2a;
    --body-ink: #4a4a4a;
    --muted: #777777;
    --bullet-blue: #1b5f96;
    --rule: #e3e3e3;
  }
  * { box-sizing: border-box; margin: 0; padding: 0; }
  html, body { width: 1200px; height: 921px; overflow: hidden; }
  body {
    position: relative;
    background: radial-gradient(ellipse at 50% 35%, #f7f5f2 0%, var(--page-bg) 70%, #e6e1da 100%);
    font-family: "Arimo", Arial, sans-serif;
    color: var(--body-ink);
  }
  .language {
    position: absolute; left: 988px; top: 33px;
    font-size: 12px; color: var(--ink); display: flex; align-items: center; gap: 6px;
  }
  .flag { width: 14px; height: 10px; display: inline-block; }
  .flag-it { background: linear-gradient(90deg, #2c9a45 33%, #fff 33% 66%, #d22c2c 66%); }
  .flag-en { background: #e7e7ee; border: 1px solid #c9c9d6; position: relative; }
  .flag-en::after { content: ""; position: absolute; left: 0; right: 0; top: 3px; height: 2px; background: #cc2b36; }

  .main-nav {
    position: absolute; left: 100px; top: 67px; width: 996px; height: 53px;
    background: linear-gradient(var(--nav-blue-top), var(--nav-blue-bottom));
    display: flex; align-items: stretch;
    font-family: "Cabin", sans-serif; font-weight: 600; font-size: 15px;
    box-shadow: 0 2px 4px rgba(0,0,0,.15);
  }
  .main-nav a {
    color: #fff; text-decoration: none; display: flex; align-items: center;
    padding: 0 18px;
  }
  .main-nav a.current { background: linear-gradient(#d42a36, var(--accent-red-dark)); padding: 0 22px 0 24px; }
  .main-nav a.last { margin-left: auto; padding-right: 22px; }

  .content-panel {
    position: absolute; left: 100px; top: 120px; width: 996px; height: 652px;
    background: var(--panel);
    box-shadow: 0 6px 18px rgba(0,0,0,.08);
  }
  .breadcrumb {
    position: absolute; left: 30px; top: 34px; font-size: 13px; color: var(--body-ink);
  }
  .breadcrumb .sep { color: var(--accent-red); margin: 0 8px; font-size: 11px; }
  .breadcrumb .here { color: var(--accent-red); }

  .book {
    position: absolute; left: 30px; width: 700px; height: 150px;
  }
  .book-cover { position: absolute; left: 0; top: 0; width: 124px; height: 149px; box-shadow: 0 1px 3px rgba(0,0,0,.3); }
  .cover-dark { background: linear-gradient(160deg, #2a1410, #0d0d0d 60%); }
  .cover-light { background: linear-gradient(90deg, #f39a23 0 16px, #f6f2ea 16px); }
  .cover-blue { background: linear-gradient(170deg, #1f4f8c, #0b1d3e 70%); }
  .book-title {
    position: absolute; left: 144px; top: 12px;
    font-family: "Cabin", sans-serif; font-weight: 700; font-size: 24px; color: var(--ink);
    white-space: nowrap;
  }
  .book-text {
    position: absolute; left: 144px; top: 44px; width: 490px;
    font-size: 13px; line-height: 16.5px; color: var(--body-ink);
  }
  .read-more {
    position: absolute; left: 144px; top: 116px; width: 86px; height: 25px;
    background: linear-gradient(#d22b37, var(--accent-red-dark)); color: #fff;
    font-size: 12px; display: flex; align-items: center; justify-content: center;
    border-radius: 2px; text-decoration: none;
  }

  .sidebar { position: absolute; left: 771px; top: 46px; width: 190px; }
  .side-block { padding-bottom: 22px; margin-bottom: 20px; border-bottom: 1px solid var(--rule); box-shadow: 0 8px 8px -8px rgba(0,0,0,.08); }
  .side-block:last-child { border-bottom: 0; box-shadow: none; }
  .side-block h3 { font-family: "Cabin", sans-serif; font-weight: 400; font-size: 18px; color: var(--ink); margin-bottom: 12px; }
  .side-block ul { list-style: none; }
  .side-block li { font-size: 11px; color: var(--muted); line-height: 17.5px; padding-left: 14px; position: relative; }
  .side-block li::before {
    content: ""; position: absolute; left: 0; top: 5px;
    border-left: 6px solid var(--bullet-blue); border-top: 4px solid transparent; border-bottom: 4px solid transparent;
  }

  .site-footer {
    position: absolute; left: 100px; top: 814px; font-size: 12px; color: var(--muted);
  }
  .social { position: absolute; left: 983px; top: 810px; display: flex; gap: 5px; }
  .social span { width: 24px; height: 24px; border-radius: 4px; background: #8b97a6; display: block; }
</style>
</head>
<body>
  <div class="language">Language <span class="flag flag-it"></span><span class="flag flag-en"></span></div>

  <nav class="main-nav">
    <a class="current" href="#">Biografia</a>
    <a href="#">Libri</a>
    <a href="#">Pubblicazioni scientifiche</a>
    <a href="#">Conferenze</a>
    <a href="#">Attivita didattica</a>
    <a href="#">Attivita medica</a>
    <a href="#">News</a>
    <a href="#">Link</a>
    <a class="last" href="#">Contatti</a>
  </nav>

  <main class="content-panel">
    <div class="breadcrumb">Biografia<span class="sep">&#9658;</span><span class="here">Book Listing</span></div>

    <article class="book" style="top:77px">
      <div class="book-cover cover-dark" role="img" aria-label="Book cover, dark with red illustration"></div>
      <h2 class="book-title">The Cellular Architecture of The Cortex</h2>
      <p class="book-text">Lorem ipsum dolor sit amet, consectetuer adipiscing elit, sed diam nonummy nibh euismod tincidunt ut laoreet dolore magna aliquam erat volutpat. Ut wisi enim ad minim veniam, quis nostrud exerci tation ullamcorper suscipit lobortis nisl ut aliquip ex ea commodo consequat.</p>
      <a class="read-more" href="#">Read More</a>
    </article>

    <article class="book" style="top:256px">
      <div class="book-cover cover-light" role="img" aria-label="Book cover, pale with orange spine band"></div>
      <h2 class="book-title">The Cellular Architecture of The Cortex</h2>
      <p class="book-text">Lorem ipsum dolor sit amet, consectetuer adipiscing elit, sed diam nonummy nibh euismod tincidunt ut laoreet dolore magna aliquam erat volutpat. Ut wisi enim ad minim veniam, quis nostrud exerci tation ullamcorper suscipit lobortis nisl ut aliquip ex ea commodo consequat.</p>
      <a class="read-more" href="#">Read More</a>
    </article>

    <article class="book" style="top:435px">
      <div class="book-cover cover-blue" role="img" aria-label="Book cover, deep blue with medical imagery"></div>
      <h2 class="book-title">The Cellular Architecture of The Cortex</h2>
      <p class="book-text">Lorem ipsum dolor sit amet, consectetuer adipiscing elit, sed diam nonummy nibh euismod tincidunt ut laoreet dolore magna aliquam erat volutpat. Ut wisi enim ad minim veniam, quis nostrud exerci tation ullamcorper suscipit lobortis nisl ut aliquip ex ea commodo consequat.</p>
      <a class="read-more" href="#">Read More</a>
    </article>

    <aside class="sidebar">
      <section class="side-block">
        <h3>Libri</h3>
        <ul><li>Lorem ipsum dolor sit amet</li><li>Consectetuer adipiscing elit</li><li>Sed diam nonummy nibh</li></ul>
      </section>
      <section class="side-block">
        <h3>Pubblicazioni scientifiche</h3>
        <ul><li>Lorem ipsum dolor sit amet</li><li>Consectetuer adipiscing elit</li><li>Sed diam nonummy nibh</li></ul>
      </section>
      <section class="side-block">
        <h3>Conferenze</h3>
        <ul><li>Lorem ipsum dolor sit amet</li><li>Consectetuer adipiscing elit</li><li>Sed diam nonummy nibh</li></ul>
      </section>
    </aside>
  </main>

  <footer class="site-footer">© 2011 Prof. Benedetto L. Caramuzza. All rights reserved.</footer>
  <div class="social" aria-label="Social links"><span></span><span></span><span></span><span></span></div>
</body>
</html>
```